"Breathe & Bloom" Book Cover 5.5x8.5

Title of the book is "Breathe & Bloom"
Subtitle is "Unmasking Pricing Myths"
I've used PixelGuild on multiple occasions you can look on my Borvex page, Mark Delwitt, to see the covers I've used in the other projects I've done.
The target audience are people who have been tricked to think they can't retire because inflation, i.e. cost of living is going up so much they must work to keep up. There is no evidence of this.
And those are the people I want to reach so they can "Breathe...and Bloom."
Target Market(s)
Americans aged 55 and over who are thinking about retirement
Industry/Entity Type
Financial
Requirements
Nice to have
- Keep It Simple, Stupid is my mantra. Just make it pop out when people are browsing
Should not have
- No piggy banks. No old people sitting on a beach.

```html
<!DOCTYPE html>
<html lang="en">
<head>
<meta charset="utf-8">
<title>Breathe &amp; Bloom — Book Cover</title>
<link href="https://fonts.googleapis.com/css2?family=Montserrat:wght@700;800;900&family=Playfair+Display:wght@500&display=swap" rel="stylesheet">
<style>
  :root {
    --page-bg: #e2e2e2;
    --ink: #0d0a06;
    --title-white: #ececec;
    --accent-orange: #e0600f;
    --sky-light: #f6d472;
    --sky-gold: #f0c21c;
    --sun-amber: #d99a2e;
    --forest-dark: #3a220e;
    --ground-dark: #170b05;
  }
  * { margin: 0; padding: 0; box-sizing: border-box; }
  html, body {
    width: 1200px;
    height: 1200px;
    overflow: hidden;
    background: var(--page-bg);
  }
  .book-cover {
    position: absolute;
    left: 224px;
    top: 50px;
    width: 752px;
    height: 1100px;
    overflow: hidden;
  }
  .cover-photo {
    position: absolute;
    inset: 0;
    background:
      radial-gradient(ellipse 22% 14% at 62% 40%, rgba(255,236,150,0.9), rgba(255,236,150,0) 70%),
      linear-gradient(90deg, rgba(26,12,4,0.85) 0%, rgba(26,12,4,0) 35%, rgba(26,12,4,0) 62%, rgba(26,12,4,0.85) 100%),
      linear-gradient(180deg, var(--sky-light) 0%, var(--sky-gold) 30%, var(--sun-amber) 45%, var(--forest-dark) 65%, var(--ground-dark) 100%);
  }
  .author-name {
    position: absolute;
    top: 30px;
    left: 0;
    width: 100%;
    text-align: center;
    font-family: "Montserrat", sans-serif;
    font-weight: 800;
    font-size: 33px;
    letter-spacing: 1px;
    color: var(--ink);
  }
  .author-rule {
    position: absolute;
    top: 95px;
    left: 61px;
    width: 636px;
    height: 1.5px;
    background: var(--ink);
  }
  .subtitle {
    position: absolute;
    top: 116px;
    left: 0;
    width: 100%;
    text-align: center;
    font-family: "Montserrat", sans-serif;
    font-weight: 700;
    font-size: 62px;
    line-height: 72px;
    color: var(--ink);
  }
  .title-art {
    position: absolute;
    inset: 0;
  }
  .title-word {
    font-family: "Montserrat", sans-serif;
    font-weight: 800;
    fill: var(--title-white);
  }
  .title-amp {
    font-family: "Playfair Display", serif;
    font-weight: 500;
    fill: var(--accent-orange);
  }
</style>
</head>
<body>
  <main class="book-cover">
    <div class="cover-photo" role="img" aria-label="Photograph of a straight country road running between tall dark tree lines toward a golden sunset over hazy mountains"></div>
    <p class="author-name">MARK DELWITT</p>
    <div class="author-rule"></div>
    <h2 class="subtitle">Unmasking<br>Pricing<br>Myths</h2>
    <svg class="title-art" viewBox="0 0 752 1100" width="752" height="1100" aria-label="Breathe &amp; Bloom">
      <text class="title-word" x="94" y="787" font-size="222" textLength="618" lengthAdjust="spacingAndGlyphs">BREATHE</text>
      <text class="title-amp" x="416" y="870" font-size="235" text-anchor="middle">&amp;</text>
      <text class="title-word" x="94" y="1016" font-size="240" textLength="618" lengthAdjust="spacingAndGlyphs">BLOOM</text>
    </svg>
  </main>
</body>
</html>
```